Web design for software company

I'm a software developer that designs high end specialist web applications, mobile apps and user friendly applications for medium to large customers. I integrate different systems together within a company and provide web based applications or mobile apps to view and edit information in that web of linked systems.

I currently work alone, basically selling my time on specialist projects, but also build my own software solutions which I eventually want to put into the market.

My company name is Overthread (lowercase 'L' for logic) and I work from the Netherlands. I've attached my current logo which is basically just text in VOXbox font. Current colours are mustard yellow and grey, but i'm open to other options to better fit the web design.

I've got a sort of slogan: "Specialized software development" - better ideas are welcome. The slogan in the logo attachment is older.

I'm looking for a site design that reflects my work as being on the cutting edge of technology, but being clear and simple. My thinking with the name Overthread is that it refers to the underlying mechanism and logic of software.

The site will not be text heavy, so some kind of large graphic to do with software design is welcome. I expect about 4 or 5 main pages or sections of the site in which i'll eventually add things like a blog or contact info etc.

Industry/Entity Type

It Company

Number of Pages Required

1 page

Font styles to use
Sans Serif

Requirements
Nice to have
• A large graphic or photo relevant to my focus as a software developer. Something that shows connecting of software systems with perhaps a variety of devices/browsers that would display data from that cloud of systems.
• Something like these (allthough these are ugly - but the idea is what i mean):
• http://img4.pixvaultimages.example/2000517/22458/i/450/pixvault_224581133-Cloud-computing-user-interface.jpg
• http://business.tamblinet.example/images/modules/mobile-device-policy-design-banner.png
• https://www.pagecraftly.example/images/responsive-web-design.jpg
• http://www.norvexa.example/images/web_apps.png
• https://www.keyportal.example/assets/img/product/web-app@2x.png?v2
Should not have
• Photographs of smiling happy people looking at a screen that make it look like it's a huge business with many offices. I'm a one-man company which could perhaps grow a little bit, but i want to focus on my expertise instead of size.

```html
<!DOCTYPE html>
<html lang="en">
<head>
<meta charset="utf-8">
<title>Overthread — Recent Projects and Blog</title>
<link rel="stylesheet" href="https://fonts.googleapis.com/css2?family=Montserrat:ital,wght@0,400;0,600;0,700;1,400&family=Open+Sans:wght@400;600;700&family=PT+Sans+Narrow&display=swap">
<style>
  :root {
    --brand-blue: #0b8bd3;
    --brand-blue-deep: #0a7cc0;
    --navy: #1b2b4b;
    --page-bg: #f6f7f9;
    --white: #ffffff;
    --ink: #1e1e1e;
    --muted: #4a4f57;
    --card-border: #e4e7eb;
    --tile-1: #3f8a46;
    --tile-2: #6a9cc0;
    --tile-3: #c9a47c;
    --tile-4: #1b3a6b;
  }
  * { margin: 0; padding: 0; box-sizing: border-box; }
  html, body { width: 1120px; height: 1200px; overflow: hidden; }
  body { position: relative; background: var(--page-bg); font-family: "Open Sans", sans-serif; color: var(--ink); }

  .band { position: absolute; left: 0; top: 0; }

  .section-title {
    position: absolute; left: 0; width: 1120px; text-align: center;
    font-family: "Montserrat", sans-serif; font-weight: 600; font-size: 24px; letter-spacing: 0.2px;
  }
  .section-title strong { font-weight: 700; }
  .section-rule { position: absolute; height: 1px; }
  .section-tagline {
    position: absolute; left: 0; width: 1120px; text-align: center;
    font-family: "Montserrat", sans-serif; font-style: italic; font-size: 11.5px;
  }

  /* Projects */
  .projects-title { top: 146px; color: var(--white); }
  .projects-rule { top: 178px; left: 393px; width: 336px; background: rgba(255,255,255,0.45); }
  .projects-tagline { top: 185px; color: #16324f; }

  .filter { position: absolute; top: 224px; font-family: "Open Sans", sans-serif; font-weight: 700; font-size: 13px; color: var(--white); line-height: 28px; }
  .filter--active { border: 1.5px solid var(--white); width: 77px; text-align: center; border-radius: 1px; }

  .project-tile { position: absolute; top: 273px; width: 280px; height: 172px; }
  .tile-1 { left: 0; background: linear-gradient(160deg, #2f3b3c 0%, var(--tile-1) 35%, #d8dde0 100%); }
  .tile-2 { left: 280px; background: linear-gradient(150deg, #86b2d2 0%, var(--tile-2) 60%, #4e84ab 100%); }
  .tile-3 { left: 560px; background: linear-gradient(140deg, #b07f55 0%, var(--tile-3) 45%, #ece6dc 100%); }
  .tile-4 { left: 840px; background: linear-gradient(170deg, #0c1e3c 0%, var(--tile-4) 50%, #2f6fb3 100%); }
  .tile-icon { position: absolute; left: 104px; top: 50px; }

  .project-caption { position: absolute; top: 458px; width: 280px; text-align: center; color: var(--white); }
  .project-caption h3 { font-family: "Montserrat", sans-serif; font-weight: 600; font-size: 16px; line-height: 22px; }
  .project-caption p { font-family: "Montserrat", sans-serif; font-size: 11px; line-height: 16px; }

  .carousel-nav { position: absolute; left: 540px; top: 538px; }

  /* Blog */
  .blog-title { top: 762px; color: var(--navy); }
  .blog-title strong { color: var(--brand-blue); }
  .blog-rule { top: 793px; left: 392px; width: 331px; background: var(--brand-blue); }
  .blog-tagline { top: 798px; color: var(--navy); }

  .feature-photo { position: absolute; left: 151px; top: 850px; width: 311px; height: 213px;
    background: radial-gradient(circle at 60% 40%, #5aa7d6 0%, #2b4a6e 35%, #16243a 100%); }
  .feature-body { position: absolute; left: 462px; top: 849px; width: 294px; height: 214px; background: var(--white); border: 1px solid var(--card-border); border-left: none; padding: 16px 14px 0 15px; }
  .post-date { font-family: "PT Sans Narrow", sans-serif; font-size: 9.5px; color: var(--muted); line-height: 12px; }
  .feature-body h4 { font-family: "Montserrat", sans-serif; font-weight: 600; font-size: 16px; color: var(--brand-blue); margin-top: 4px; line-height: 20px; }
  .feature-body p { font-size: 10.4px; line-height: 17px; color: var(--ink); margin-top: 2px; }
  .feature-body p + p { margin-top: 16px; }
  .read-more { display: inline-block; margin-top: 7px; font-size: 10.5px; font-weight: 700; color: var(--brand-blue); text-decoration: underline; }

  .side-photo { position: absolute; left: 767px; top: 849px; width: 202px; height: 107px;
    background: linear-gradient(160deg, #f2f2f2 0%, #d9dadc 50%, #8d2232 75%, #c9cbce 100%); }
  .side-photo .post-date { position: absolute; left: 0; bottom: 0; width: 100%; height: 36px; background: rgba(60,66,78,0.85); color: #e8eaee; padding: 10px 0 0 13px; }
  .side-card { position: absolute; left: 768px; top: 968px; width: 202px; height: 94px; background: var(--brand-blue); color: var(--white); padding: 11px 10px 0 11px; }
  .side-card h4 { font-family: "Montserrat", sans-serif; font-weight: 600; font-size: 13.5px; line-height: 16px; }
  .side-card p { font-size: 9.2px; line-height: 13.6px; margin-top: 3px; }
</style>
</head>
<body>
  <svg class="band" width="1120" height="1200" aria-hidden="true">
    <polygon points="0,58 808,0 1120,0 1120,590 0,669" fill="var(--brand-blue)"/>
    <polygon points="384,1200 1120,1148 1120,1200" fill="var(--brand-blue)"/>
  </svg>

  <section class="projects">
    <h2 class="section-title projects-title">RECENT <strong>PROJECTS</strong></h2>
    <div class="section-rule projects-rule"></div>
    <p class="section-tagline projects-tagline">With a motivated team, excellent capabilities and experience</p>

    <span class="filter" style="left:338px">Teampoint</span>
    <span class="filter filter--active" style="left:419px">Ledgera</span>
    <span class="filter" style="left:509px">Front-end Development</span>
    <span class="filter" style="left:698px">IT Consulting</span>

    <div class="project-tile tile-1" role="img" aria-label="Website analytics dashboard on a laptop screen"></div>
    <div class="project-tile tile-2" role="img" aria-label="Laptop keyboard under a blue hover overlay">
      <svg class="tile-icon" width="72" height="72" viewBox="0 0 72 72" aria-hidden="true">
        <circle cx="36" cy="36" r="36" fill="#2a3340" opacity="0.92"/>
        <path d="M41 27 L29 39 a4 4 0 0 0 6 6 L47 33 a7 7 0 0 0 -10 -10 L25 35 a10 10 0 0 0 14 14 L47 41" fill="none" stroke="#fff" stroke-width="2.4" stroke-linecap="round"/>
      </svg>
    </div>
    <div class="project-tile tile-3" role="img" aria-label="Hands arranging paper wireframe sketches on a desk"></div>
    <div class="project-tile tile-4" role="img" aria-label="Hosting company website shown on a monitor"></div>

    <div class="project-caption" style="left:9px"><h3>Consulting Project</h3><p>IT Consulting</p></div>
    <div class="project-caption" style="left:276px"><h3>Project name</h3><p>Category name</p></div>
    <div class="project-caption" style="left:568px"><h3>Consulting Project</h3><p>IT Consulting</p></div>
    <div class="project-caption" style="left:838px"><h3>Velnor Developement</h3><p>Ledgera Development</p></div>

    <svg class="carousel-nav" width="40" height="22" viewBox="0 0 40 22" aria-hidden="true">
      <polyline points="12,2 4,11 12,20" fill="none" stroke="rgba(255,255,255,0.4)" stroke-width="2"/>
      <polyline points="24,2 32,11 24,20" fill="none" stroke="#fff" stroke-width="2"/>
    </svg>
  </section>

  <section class="blog">
    <h2 class="section-title blog-title">RECENT <strong>BLOG</strong></h2>
    <div class="section-rule blog-rule"></div>
    <p class="section-tagline blog-tagline">With a motivated team, excellent capabilities and experience</p>

    <div class="feature-photo" role="img" aria-label="Finger touching a glowing network of connected device icons"></div>
    <article class="feature-body">
      <p class="post-date">SEPTEMBER 20, 2015. 3:20 PM</p>
      <h4>TITLE OF THE BLOG</h4>
      <p>Lorem ipsum dolor sit amet, consectetur adipisicing elit, sed do eiusmod tempor incididunt ut labore et dolore magna aliqua. We will appreciate your particaption in the donation drive.</p>
      <p>&nbsp;Show the first 5 donation levels, and the highest Show the first events.</p>
      <a class="read-more">Continue Reading</a>
    </article>

    <div class="side-photo" role="img" aria-label="Tablet and phone on a desk beside a coffee cup">
      <p class="post-date">SEPTEMBER 20, 2015. 3:20 PM</p>
    </div>
    <article class="side-card">
      <h4>TITLE OF THE BLOG</h4>
      <p>We will write the news in brief details here. We will write the news in brief details here. We will write the news in brief details here.</p>
    </article>
  </section>
</body>
</html>
```